Velmora, Inc. Website

Looking for a website design and build for Velmora, Inc. an intellectual property incubator for the recreational and medical cannabis space in California. Our logo and brand identity has been completed website so w can begin our SEO leg of brand development.

See more details in Must haves and Nice to Haves

Target Market(s)

Target market

Vision

Our proprietary ideas have been developed to shift the approach on how whole body wellness and healing is achieved. Velmora's patent pending designs and formulations are rooted in the desire to find the most efficient, customizable, and convenient  method to precisely micro-despense whole plant cannabis extracts. 

Our ideas, designs and development team are supported by leading chemists specializing in cannabis extraction technology, leading medical doctors collaborating to develop our proprietary cannabis formulations and a passion to shift landscape of healing from a dependency on isolated symptom treatment to whole body, whole plant, whole life wellness for ourselves and our families. 

Goal

Develop, patent, and trademark our proprietary devices, formulations, and ideas for the purpose of licensing, manufacturing and distributing in the Cannabis Industry.

Industry/Entity Type

Medical

Coding

Coded - Design and coding required

Number of Pages Required

5+ page

Font styles to use
Other font styles liked:
• See Brand Identity Guide

Requirements
Must have
• Look and Feel: We are developing products, intellectual property and platforms to bring together the medical, health & wellness, and cannabis industries to provide individuals and families alike a innovative solutions to chronic illness, mood disorders, and over all wellbeing.
• Page Titles
• Home - Landing Page
• Vision-
• IP Technology & Products - will remain under construction
• Team
• Strategic Partners – will remain under construction
• Invest- will need a form to aquire contact information as well as have some questions that need to be answered to help evaluate to the potential interested party
• Contact Us– Velmora address and info@ email
Nice to have
• Images - wellness, balance, health, healing, herbs, not just cannabis, aromatherapy, mediation, energy work, dna, scientific research, microdosing, medical testing
• Style sleek and innovative - cutting edge technology - inspire to learn more
• For Colors and Fonts - See Brand Identity Guide
• Site layouts that we like are:
• http://www.example-tarnwick.com
• https://www.example-plovisandcare.com
• https://www.example-durnique.com
• https://www.example-zobra.com
• https://www.example-quessa.com
Should not have
• Should not have to many cannabis images - imagery should balanced between cannabis, medical & recreational, health and wellness, mental health

```html
<!DOCTYPE html>
<html lang="en">
<head>
<meta charset="utf-8">
<title>Velmora — Recreational and medical cannabis space in California</title>
<link rel="stylesheet" href="https://fonts.googleapis.com/css2?family=Jost:wght@400;500;600;700&family=Great+Vibes&display=swap">
<style>
  :root {
    --purple: #6b2d83;
    --purple-dark: #4e1f61;
    --green: #3a9a1e;
    --ink: #1e1e1e;
    --muted: #7a7a7a;
    --light: #f2f2f2;
    --white: #ffffff;
    --rule: #d9a7cf;
  }
  * { box-sizing: border-box; margin: 0; padding: 0; }
  html, body { width: 1200px; height: 3249px; overflow: hidden; background: var(--white); }
  body { font-family: "Jost", "Helvetica Neue", Arial, sans-serif; color: var(--ink); position: relative; }
  .page { position: relative; width: 1200px; height: 3249px; overflow: hidden; }

  /* Navigation */
  .site-nav { position: absolute; top: 0; left: 0; width: 1200px; height: 66px; background: var(--white); z-index: 5; }
  .site-nav a { position: absolute; top: 37px; font-size: 11.5px; font-weight: 700; color: var(--ink); text-decoration: none; letter-spacing: .3px; transform: translateX(-50%); white-space: nowrap; }
  .brand-badge { position: absolute; left: 544px; top: 4px; width: 112px; height: 112px; border-radius: 50%; background: var(--white); border: 4px solid var(--white); box-shadow: 0 2px 6px rgba(0,0,0,.15); z-index: 6; display: flex; align-items: center; justify-content: center; }
  .brand-badge .ring { width: 96px; height: 96px; border-radius: 50%; border: 3px solid var(--purple); display: flex; align-items: center; justify-content: center; }
  .brand-name { font-family: "Jost", sans-serif; font-weight: 700; color: var(--purple); font-size: 14px; letter-spacing: 1px; }

  /* Hero */
  .hero { position: absolute; top: 66px; left: 0; width: 1200px; height: 524px; overflow: hidden; }
  .hero-photo { position: absolute; inset: 0; background: linear-gradient(100deg, #8a7b6e 0%, #a79a8c 30%, #6e6560 60%, #3b3533 100%); }
  .hero-curve { position: absolute; top: 0; left: 0; }
  .hero-title { position: absolute; top: 170px; width: 100%; text-align: center; color: var(--white); font-size: 96px; font-weight: 600; letter-spacing: 2px; line-height: 1; }
  .hero-sub { position: absolute; top: 279px; width: 100%; text-align: center; color: var(--white); font-size: 27px; font-weight: 400; }
  .btn { display: inline-flex; align-items: center; justify-content: center; background: var(--purple); color: var(--white); font-size: 12px; font-weight: 700; border-radius: 26px; text-decoration: none; letter-spacing: .5px; }
  .hero .btn { position: absolute; left: 511px; top: 339px; width: 178px; height: 52px; }

  /* Section headings */
  .script { font-family: "Great Vibes", cursive; font-size: 50px; color: var(--purple-dark); text-align: center; line-height: 1; }
  .brand-heading { font-size: 34px; font-weight: 700; color: var(--green); text-align: center; letter-spacing: 1px; line-height: 1; }
  .divider { width: 90px; height: 2px; background: var(--rule); margin: 0 auto; }

  /* Welcome */
  .welcome { position: absolute; top: 590px; left: 0; width: 1200px; height: 510px; background: var(--light); }
  .welcome .script { position: absolute; top: 28px; width: 100%; }
  .welcome .brand-heading { position: absolute; top: 86px; width: 100%; }
  .welcome .divider { position: absolute; top: 150px; left: 555px; }
  .welcome p { position: absolute; left: 240px; width: 720px; text-align: center; font-size: 13px; line-height: 24px; color: var(--muted); }
  .welcome .p1 { top: 186px; }
  .welcome .p2 { top: 282px; }
  .welcome .btn { position: absolute; left: 511px; top: 378px; width: 178px; height: 52px; }
  .welcome-curve { position: absolute; top: 1040px; left: 0; }

  /* Services */
  .services { position: absolute; top: 1100px; left: 0; width: 1200px; height: 680px; }
  .services .script { position: absolute; top: 75px; width: 100%; }
  .services .brand-heading { position: absolute; top: 128px; width: 100%; }
  .services .divider { position: absolute; top: 191px; left: 555px; background: #cfcfcf; }
  .service-card { position: absolute; top: 226px; width: 488px; height: 327px; overflow: hidden; color: var(--white); }
  .service-card.recreational { left: 95px; }
  .service-card.space { left: 609px; }
  .card-photo { position: absolute; inset: 0; }
  .recreational .card-photo { background: linear-gradient(135deg, #8a3f95 0%, #6b2d83 55%, #4f2a4a 100%); }
  .space .card-photo { background: linear-gradient(135deg, #4aa52a 0%, #3a9a1e 55%, #2a6e18 100%); }
  .card-body { position: absolute; left: 33px; top: 40px; width: 420px; }
  .card-body h3 { font-size: 28px; font-weight: 600; margin-bottom: 18px; }
  .card-body p { font-size: 10.5px; line-height: 15.5px; margin-bottom: 12px; opacity: .92; }
  .btn-outline { display: inline-flex; align-items: center; justify-content: center; width: 112px; height: 30px; border: 2px solid var(--white); border-radius: 16px; color: var(--white); font-size: 10.5px; font-weight: 700; text-decoration: none; margin-top: 8px; }

  /* Testimonials */
  .testimonials { position: absolute; top: 1780px; left: 0; width: 1200px; height: 620px; background: var(--light); }
  .testimonials .script { position: absolute; top: 104px; width: 100%; }
  .testimonials .brand-heading { position: absolute; top: 158px; width: 100%; }
  .avatar { position: absolute; left: 194px; top: 262px; width: 240px; height: 240px; border-radius: 50%; border: 7px solid var(--purple); background: linear-gradient(160deg, #9a8a7a 0%, #5f5450 60%, #33415a 100%); box-shadow: 0 18px 22px -14px rgba(0,0,0,.35); }
  .quote { position: absolute; left: 494px; top: 288px; width: 480px; }
  .quote h4 { font-size: 33px; font-weight: 600; color: var(--green); line-height: 1.1; }
  .quote .role { font-size: 13px; color: var(--muted); margin: 6px 0 24px; }
  .quote p { font-size: 13px; line-height: 24px; color: var(--muted); }
  .dots { position: absolute; top: 566px; left: 560px; display: flex; gap: 14px; }
  .dots span { width: 9px; height: 9px; border-radius: 50%; background: #c8c8c8; }
  .dots span.active { background: var(--purple); }

  /* Locator */
  .locator { position: absolute; top: 2376px; left: 0; width: 1200px; height: 559px; overflow: hidden; }
  .map { position: absolute; inset: 0; background: linear-gradient(120deg, #cfcfcf 0%, #bdbdbd 40%, #d6d6d6 70%, #c4c4c4 100%); }
  .locator svg.curves { position: absolute; inset: 0; }
  .find-pill { position: absolute; left: 425px; top: 248px; width: 353px; height: 78px; background: var(--white); border-radius: 40px; box-shadow: 0 3px 10px rgba(0,0,0,.2); display: flex; align-items: center; }
  .find-pill .mini-badge { width: 70px; height: 70px; margin-left: 4px; border-radius: 50%; border: 3px solid var(--purple); display: flex; align-items: center; justify-content: center; }
  .find-pill .mini-badge span { font-size: 10px; font-weight: 700; color: var(--purple); }
  .find-pill strong { font-size: 22px; font-weight: 600; color: #444; margin-left: 20px; }
  .find-pill svg { margin-left: 26px; }

  /* Footer */
  .site-footer { position: absolute; top: 2935px; left: 0; width: 1200px; height: 314px; background: var(--white); }
  .footer-badge { position: absolute; left: 123px; top: 67px; width: 140px; height: 140px; border-radius: 50%; border: 4px solid var(--purple); display: flex; align-items: center; justify-content: center; }
  .footer-badge .brand-name { font-size: 19px; }
  .footer-col { position: absolute; top: 58px; }
  .footer-col h5 { font-size: 11.5px; font-weight: 700; margin-bottom: 10px; }
  .footer-col a { display: block; font-size: 11px; color: var(--ink); text-decoration: none; line-height: 25.5px; }
  .col-quick { left: 364px; }
  .col-other { left: 565px; }
  .col-contact { left: 801px; }
  .phone { display: flex; align-items: center; gap: 6px; font-size: 15px; margin: 4px 0 24px; }
  .socials { display: flex; gap: 8px; margin-top: 10px; }
  .socials span { width: 27px; height: 27px; border-radius: 50%; background: var(--ink); }
  .socials span:first-child { background: var(--purple); }
  .footer-rule { position: absolute; top: 249px; left: 0; width: 1200px; height: 1px; background: #e2e2e2; }
  .copyright { position: absolute; top: 278px; width: 100%; text-align: center; font-size: 11px; }
</style>
</head>
<body>
<div class="page">

  <nav class="site-nav">
    <a href="#" style="left:120px">HOME</a>
    <a href="#" style="left:238px">VISION</a>
    <a href="#" style="left:400px">IP TECHNOLOGY</a>
    <a href="#" style="left:712px">TEAM</a>
    <a href="#" style="left:840px">STRATEGIC PARTNERS</a>
    <a href="#" style="left:972px">INVEST</a>
    <a href="#" style="left:1080px">CONTACT US</a>
  </nav>
  <div class="brand-badge"><div class="ring"><span class="brand-name">VELMORA</span></div></div>

  <header class="hero">
    <div class="hero-photo" role="img" aria-label="Photo of a scientist in protective gear working in a laboratory"></div>
    <svg class="hero-curve" width="1200" height="30" viewBox="0 0 1200 30" aria-hidden="true">
      <path d="M0 0 H1200 V0 Q600 40 0 12 Z" fill="#ffffff"/>
    </svg>
    <h1 class="hero-title">VELMORA</h1>
    <p class="hero-sub">Recreational and medical cannabis space in California</p>
    <a class="btn" href="#">LEARN MORE</a>
  </header>

  <section class="welcome">
    <div class="script">Welcome to</div>
    <div class="brand-heading">VELMORA</div>
    <div class="divider"></div>
    <p class="p1">Velmora, Inc. is an intellectual property incubator for the recreational and medical cannabis space in California. Our proprietary ideas have been developed to shift the approach on how whole body wellness and healing is achieved, bringing together the medical, health and wellness, and cannabis industries for individuals and families alike.</p>
    <p class="p2">Our patent pending designs and formulations are rooted in the desire to find the most efficient, customizable, and convenient method to precisely micro-dispense whole plant cannabis extracts.</p>
    <a class="btn" href="#">LEARN MORE</a>
  </section>
  <svg class="welcome-curve" width="1200" height="70" viewBox="0 0 1200 70" aria-hidden="true">
    <path d="M0 0 H1200 V20 Q600 95 0 20 Z" fill="#f2f2f2"/>
  </svg>

  <section class="services">
    <div class="script">What We Provide</div>
    <div class="brand-heading">VELMORA</div>
    <div class="divider"></div>

    <article class="service-card recreational">
      <div class="card-photo" role="img" aria-label="Photo of dried herbs in a bowl, tinted purple"></div>
      <div class="card-body">
        <h3>Recreational</h3>
        <p>Velmora's patent pending designs are rooted in the desire to find the most efficient, customizable and convenient method to precisely micro-dispense whole plant cannabis extracts for everyday balance, mood and overall wellbeing.</p>
        <p>We develop, patent and trademark our proprietary devices and formulations for licensing, manufacturing and distribution in the cannabis industry.</p>
        <a class="btn-outline" href="#">READ MORE</a>
      </div>
    </article>

    <article class="service-card space">
      <div class="card-photo" role="img" aria-label="Photo of a plant close-up, tinted green"></div>
      <div class="card-body">
        <h3>Cannabis Space</h3>
        <p>Our team is supported by leading chemists specializing in cannabis extraction technology and medical doctors collaborating to develop proprietary formulations for chronic illness, mood disorders and whole body wellness.</p>
        <p>We aim to shift healing from isolated symptom treatment to whole body, whole plant, whole life wellness for ourselves and our families.</p>
        <a class="btn-outline" href="#">READ MORE</a>
      </div>
    </article>
  </section>

  <section class="testimonials">
    <div class="script">Our Customers In</div>
    <div class="brand-heading">VELMORA</div>
    <div class="avatar" role="img" aria-label="Portrait photo of the customer"></div>
    <div class="quote">
      <h4>Marcus Delane</h4>
      <div class="role">Company Name</div>
      <p>Velmora brings a fresh, science-led approach to wellness. Their focus on precise, whole plant formulations and careful research gave our family real confidence, and their team was open, thoughtful and ready to answer every question along the way.</p>
    </div>
    <div class="dots"><span class="active"></span><span></span><span></span><span></span></div>
  </section>

  <section class="locator">
    <div class="map" role="img" aria-label="Grey road map of California and the western United States"></div>
    <svg class="curves" width="1200" height="559" viewBox="0 0 1200 559" aria-hidden="true">
      <path d="M0 0 H1200 V28 Q600 -10 0 28 Z" fill="#f2f2f2"/>
      <path d="M0 559 H1200 V520 Q600 590 0 520 Z" fill="#ffffff"/>
    </svg>
    <div class="find-pill">
      <div class="mini-badge"><span>VELMORA</span></div>
      <strong>Find Your Location</strong>
      <svg width="14" height="22" viewBox="0 0 14 22" aria-hidden="true"><path d="M3 3 L11 11 L3 19" fill="none" stroke="#3a9a1e" stroke-width="3.5" stroke-linecap="round" stroke-linejoin="round"/></svg>
    </div>
  </section>

  <footer class="site-footer">
    <div class="footer-badge"><span class="brand-name">VELMORA</span></div>
    <div class="footer-col col-quick">
      <h5>Quick Links</h5>
      <a href="#">Home</a><a href="#">Vision</a><a href="#">IP Technology</a><a href="#">Team</a><a href="#">Invest</a><a href="#">Contact Us</a>
    </div>
    <div class="footer-col col-other">
      <h5>Other Links</h5>
      <a href="#">Terms Of Service</a><a href="#">Privacy Policy</a><a href="#">Help</a><a href="#">Disclaimer</a>
    </div>
    <div class="footer-col col-contact">
      <h5>Contact Us</h5>
      <div class="phone">
        <svg width="20" height="20" viewBox="0 0 20 20" aria-hidden="true"><circle cx="10" cy="10" r="8.5" fill="none" stroke="#3a9a1e" stroke-width="1.8"/><path d="M7 5.5 L8.6 7.6 L7.8 8.8 Q9 11.2 11.2 12.2 L12.4 11.4 L14.5 13 L13.6 14.5 Q9.5 14.5 5.5 8.2 Z" fill="#3a9a1e"/></svg>
        1-800-555-0147
      </div>
      <h5>Connect With Us</h5>
      <div class="socials"><span></span><span></span><span></span></div>
    </div>
    <div class="footer-rule"></div>
    <div class="copyright">© 2017 Company Name | All Rights Reserved</div>
  </footer>

</div>
</body>
</html>
```